Cannabis Processor Vape Cart Box Design/Concentrate Jar Box Design

We are a solventless (no chemicals added) cannabis processor in the state of Michigan. We have 2 products, one is a vape cartridge and one is a 5mL clear glass concentrate jar with a black lid. We need designs that correlates with our logo for their box packaging. Each piece of packaging has an opening so you can see the jar/vape cartridge and their contents. Each piece of packaging needs to have the universal symbol of cannabis, which is on the bottom right hand corner of the vape cartridge container for reference. Also on the jar box top lid we need the net weight listed like this (NET WT. 1.0g / 0.0176oz) I have attached some examples of the packaging boxes, the jar we will be using, and our logo so you know what you are shooting for. On the Jar Box there will be a hole in the center of the bottom of the box, so people can see the jar and it's contents. On the back of the jar box I would like the following (Here at 582 Resinworks, our mission is to be make the purest concentrates available. We strive to fully represent the true essence of the flower through our solventless processes. At 582 Resinworks we only use the finest Michigan grown, pesticide-free flowers for extraction. We pride ourselves on our chemical-free extraction methods, and are constantly innovating to bring better and cleaner concentrates for Medicinal and Recreational use.) On the Vape Cartridge box there will be a straight up and down hole in the shape of the vape cartridge instead of the Michigan shape. Get creative, but remember that you can not use any cannabis leaf symbol on the design. On the top of the back of the vape cartridge box I want the following (Here at 582 Resinworks, our mission is to be make the purest vape cartridge available. We strive to fully represent the true essence of the flower through our solventless processes. At 582 Resinworks we only use the finest Michigan grown, pesticide-free flowers for extraction. We pride ourselves on our chemical-free extraction methods, and are constantly innovating to bring better and cleaner products for both Medicinal and Recreational use.) We look forward to your submissions, and to the best design we thank you in advance. I almost forgot, we would prefer a black base with white lettering, but we are open to any creative ideas, so please submit more options than what we requested, because the best look will win.

```html
<!DOCTYPE html>
<html lang="en">
<head>
<meta charset="UTF-8">
<title>582 Resinworks – Premium Vape Box Dieline</title>
<link rel="stylesheet" href="https://fonts.googleapis.com/css2?family=Lato:wght@400;700&family=Roboto:wght@700&display=swap">
<style>
  :root {
    --bg-top: #000000;
    --bg-bottom: #232323;
    --panel: #0d0d0d;
    --panel-edge: #1b1b1b;
    --gold-light: #fff6d6;
    --gold: #c29a12;
    --gold-deep: #5a4310;
    --oil: #e8c988;
    --ink: #ffffff;
  }
  * { margin: 0; padding: 0; box-sizing: border-box; }
  html, body { width: 1200px; height: 1107px; overflow: hidden; }
  body {
    position: relative;
    background: linear-gradient(180deg, var(--bg-top) 0%, var(--bg-bottom) 100%);
    font-family: "Lato", sans-serif;
    color: var(--ink);
  }
  .dieline { position: absolute; inset: 0; }
  .dieline svg { position: absolute; left: 0; top: 0; }
  .label { position: absolute; white-space: nowrap; }
  .brand {
    font-family: "Lato", sans-serif;
    font-weight: 400;
    font-size: 14px;
    letter-spacing: 1.5px;
    color: var(--ink);
  }
  .brand-vertical { writing-mode: vertical-rl; }
  .product-name {
    font-family: "Roboto", sans-serif;
    font-weight: 700;
    font-size: 14px;
    line-height: 17px;
  }
  .product-name-vertical { writing-mode: vertical-rl; font-size: 13px; line-height: 17px; }
  .volume { font-family: "Lato", sans-serif; font-size: 13px; }
  .mission {
    position: absolute;
    left: 984px; top: 354px; width: 168px;
    text-align: center;
    font-size: 12px;
    line-height: 15px;
  }
</style>
</head>
<body>
<main class="dieline">
  <svg width="1200" height="1107" viewBox="0 0 1200 1107" aria-hidden="true">
    <defs>
      <linearGradient id="hangTab" x1="0" y1="1" x2="1" y2="0">
        <stop offset="0" stop-color="var(--gold-deep)"/>
        <stop offset="0.4" stop-color="var(--gold)"/>
        <stop offset="0.7" stop-color="var(--gold-light)"/>
        <stop offset="1" stop-color="var(--gold)"/>
      </linearGradient>
      <linearGradient id="goldBand" x1="636" y1="683" x2="978" y2="392" gradientUnits="userSpaceOnUse">
        <stop offset="0" stop-color="var(--gold-deep)"/>
        <stop offset="0.25" stop-color="var(--gold)"/>
        <stop offset="0.5" stop-color="var(--gold-light)"/>
        <stop offset="0.75" stop-color="var(--gold)"/>
        <stop offset="1" stop-color="var(--gold-light)"/>
      </linearGradient>
      <linearGradient id="panelShade" x1="0" y1="0" x2="1" y2="0">
        <stop offset="0" stop-color="var(--panel-edge)"/>
        <stop offset="0.5" stop-color="var(--panel)"/>
        <stop offset="1" stop-color="var(--panel-edge)"/>
      </linearGradient>
      <linearGradient id="oilFill" x1="0" y1="0" x2="1" y2="0">
        <stop offset="0" stop-color="#b99a5c"/>
        <stop offset="0.3" stop-color="var(--oil)"/>
        <stop offset="0.6" stop-color="#f3dcaa"/>
        <stop offset="1" stop-color="#a88a50"/>
      </linearGradient>
    </defs>

    <!-- hang tabs -->
    <g class="hang-tabs">
      <rect x="718" y="254" width="172" height="44" fill="url(#hangTab)"/>
      <rect x="979" y="254" width="172" height="44" fill="url(#hangTab)"/>
      <rect x="780" y="269" width="48" height="5" rx="2.5" fill="#111"/>
      <circle cx="804" cy="271.5" r="7" fill="#111"/>
      <rect x="1045" y="269" width="48" height="5" rx="2.5" fill="#111"/>
      <circle cx="1069" cy="271.5" r="7" fill="#111"/>
    </g>

    <!-- panels -->
    <g class="panels">
      <rect x="636" y="298" width="73" height="463" fill="url(#panelShade)"/>
      <rect x="709" y="298" width="188" height="463" fill="url(#panelShade)"/>
      <rect x="897" y="298" width="79" height="463" fill="url(#panelShade)"/>
      <rect x="976" y="298" width="183" height="463" fill="url(#panelShade)"/>
    </g>

    <!-- diagonal gold band -->
    <polygon class="gold-band" points="636,526 978,392 978,536 636,683" fill="url(#goldBand)"/>

    <!-- front window -->
    <rect class="window" x="752" y="388" width="103" height="298" fill="#151515"/>
    <g class="cartridge" role="img" aria-label="Vape cartridge filled with golden oil, seen through the window">
      <rect x="779" y="388" width="56" height="62" fill="#2a2a2a"/>
      <rect x="779" y="450" width="56" height="210" fill="url(#oilFill)"/>
    </g>

    <!-- black swoop over lower front panel -->
    <path class="front-swoop" d="M752,686 C770,630 790,600 835,596 C848,594 855,590 855,584 L897,571 L897,761 L752,761 Z" fill="var(--panel)"/>

    <!-- cannabis warning symbol placeholder -->
    <polygon class="warning-mark" points="870,711 896,737 870,763 844,737" fill="none" stroke="var(--ink)" stroke-width="2" transform="translate(0,-9) scale(1)"/>
  </svg>

  <!-- side panel 1 -->
  <div class="label brand brand-vertical" style="left:666px; top:347px;">582 Resinworks</div>
  <div class="label product-name product-name-vertical" style="left:654px; top:686px;">PREMIUM<br>VAPE</div>

  <!-- front panel -->
  <div class="label brand" style="left:752px; top:342px;">582 Resinworks</div>
  <div class="label volume" style="left:833px; top:607px;">5ML</div>
  <div class="label product-name" style="left:793px; top:647px;">PREMIUM<br>VAPE</div>

  <!-- side panel 2 -->
  <div class="label product-name product-name-vertical" style="left:918px; top:332px;">PREMIUM<br>VAPE</div>
  <div class="label brand brand-vertical" style="left:926px; top:628px;">582 Resinworks</div>

  <!-- back panel -->
  <p class="mission">Here at 582 Resinworks,<br>our mission is to be make the<br>purest vape cartridge<br>available. We strive to fully<br>represent the true essence<br>of the flower through our<br>solventless processes. At<br>582 Resinworks we only use<br>the finest Michigan<br>grown, pesticide-free<br>flowers for extraction. We<br>pride ourselves on our<br>chemical-free extraction<br>methods, and are con-<br>stantly innovating to bring<br>better and cleaner prod-<br>ucts for both Medicinal<br>and Recreational use.</p>
  <div class="label brand" style="left:1016px; top:678px;">582 Resinworks</div>
</main>
</body>
</html>
```